Megafield Party Poster 50 2016

We are looking for a designer to create A0 A3 and A4 versions of a Megafield Party Poster. The poster is for a special event we are having at the restaurant for the big game!

We have included in the brief some examples of other posters that other locations have made for both the current game and past games.

• The poster must have on it somewhere the following:
• MEGA FIELD 50
• Free Entry
• Monday, February 8th, 2016 OPEN at 9am
• 25 HD Screens
• Prize Giveaways / Breakfast Burger and Beer Breakfast Pregame / Wings, Pizzas, Beer Towers, Buckets,
• KTO940 Radio Live Crossover Onsite
• RESERVE YOUR TABLE NOW
• 1 3000 FEAST

```html
<!DOCTYPE html>
<html lang="en">
<head>
<meta charset="utf-8">
<title>Mega Field 50 Party Poster</title>
<link rel="stylesheet" href="https://fonts.googleapis.com/css2?family=League+Gothic&family=Jost:wght@400&family=Oswald:wght@400;500;600&family=Roboto+Slab:wght@700;800&display=swap">
<style>
  :root {
    --page-bg: #d9dcdb;
    --poster-black: #050505;
    --smoke: #5a5448;
    --smoke-dark: #1b1915;
    --silver-light: #f4f7fa;
    --silver-mid: #a9b6c2;
    --silver-dark: #5d6b78;
    --gold: #d6ad5c;
    --red: #ec1b3b;
    --white: #ffffff;
    --ink: #111111;
  }
  * { margin: 0; padding: 0; box-sizing: border-box; }
  html, body { width: 960px; height: 1200px; overflow: hidden; }
  body { background: var(--page-bg); position: relative; }

  .poster {
    position: absolute; left: 180px; top: 30px;
    width: 600px; height: 1140px;
    background: var(--poster-black);
    overflow: hidden;
    font-family: "Oswald", "Arial Narrow", sans-serif;
  }

  .hero-photo {
    position: absolute; left: 0; top: 0; width: 600px; height: 400px;
    background:
      radial-gradient(ellipse at 60% 25%, var(--smoke) 0%, var(--smoke-dark) 45%, transparent 75%),
      linear-gradient(180deg, var(--smoke-dark) 0%, #0d0c0a 70%, var(--poster-black) 100%);
  }

  .brand-mark {
    position: absolute; left: 38px; top: 12px; width: 150px; height: 150px;
    background: var(--white);
    border-bottom: 10px solid var(--red);
    display: flex; align-items: center; justify-content: center;
    text-align: center; padding: 12px;
  }
  .brand-name {
    font-family: "Oswald", "Arial Narrow", sans-serif;
    font-weight: 600; font-size: 22px; line-height: 1.1;
    color: var(--ink); text-transform: uppercase;
  }

  .event-title {
    position: absolute; left: 0; top: 395px; width: 600px;
    text-align: center;
    font-family: "Roboto Slab", Georgia, serif; font-weight: 800;
    background: linear-gradient(180deg, var(--silver-light) 0%, var(--silver-mid) 45%, var(--silver-dark) 55%, var(--silver-light) 100%);
    -webkit-background-clip: text; background-clip: text; color: transparent;
  }
  .event-title .title-words { display: block; font-size: 74px; line-height: 78px; letter-spacing: 1px; }
  .event-title .title-number { display: block; font-size: 232px; line-height: 205px; margin-top: 2px; }

  .free-entry {
    position: absolute; left: 178px; top: 765px; width: 272px; height: 45px;
    background: var(--gold); color: var(--ink);
    font-family: "Roboto Slab", Georgia, serif; font-weight: 800; font-size: 27px;
    display: flex; align-items: center; justify-content: center; letter-spacing: 1px;
    white-space: nowrap;
  }

  .event-date {
    position: absolute; left: 0; top: 818px; width: 600px;
    text-align: center; color: var(--red);
    font-family: "League Gothic", "Arial Narrow", sans-serif;
    font-size: 44px; line-height: 50px; text-transform: uppercase;
    white-space: nowrap; letter-spacing: 0.5px;
  }

  .star-rule {
    position: absolute; left: 19px; top: 876px; width: 562px;
    color: var(--gold); font-size: 12px; letter-spacing: 6.2px;
    white-space: nowrap; overflow: hidden; text-align: center;
  }

  .screens-badge {
    position: absolute; left: 19px; top: 912px; width: 200px; height: 206px;
    background: var(--gold); color: var(--ink);
    text-align: center; padding-top: 14px; overflow: hidden;
  }
  .screens-badge .screens-count {
    display: block; font-family: "League Gothic", "Arial Narrow", sans-serif;
    font-size: 132px; line-height: 128px; white-space: nowrap;
  }
  .screens-badge .screens-label {
    display: block; font-family: "Jost", "Futura", sans-serif;
    font-weight: 400; font-size: 38px; line-height: 46px; white-space: nowrap;
  }

  .offer-list {
    position: absolute; left: 244px; top: 898px; width: 330px;
    color: var(--white); font-size: 13px; line-height: 21px; text-transform: uppercase; font-weight: 400;
    white-space: nowrap;
  }

  .reserve-button {
    position: absolute; left: 219px; top: 987px; width: 362px; height: 50px;
    background: var(--red); color: var(--white);
    font-family: "League Gothic", "Arial Narrow", sans-serif;
    font-size: 40px; letter-spacing: 0.5px;
    display: flex; align-items: center; padding-left: 26px; text-transform: uppercase;
    white-space: nowrap;
  }

  .phone-line {
    position: absolute; left: 244px; top: 1078px;
    color: var(--white); font-size: 13px; letter-spacing: 0.5px;
  }
</style>
</head>
<body>
  <main class="poster">
    <div class="hero-photo" role="img" aria-label="Five football players in black and gold uniforms posing in front of a city skyline under smoky clouds, the quarterback raising the ball"></div>

    <div class="brand-mark">
      <span class="brand-name">The Oven &amp; Ember Company</span>
    </div>

    <h1 class="event-title">
      <span class="title-words">MEGA<br>FIELD</span>
      <span class="title-number">50</span>
    </h1>

    <div class="free-entry">FREE ENTRY</div>

    <p class="event-date">Monday, February 8th, 2016 Open at 9am</p>

    <div class="star-rule" aria-hidden="true">★★★★★★★★★★★★★★★★★★★★★★★★★★★★★★★★★★★★★★★</div>

    <div class="screens-badge">
      <span class="screens-count">25HD</span>
      <span class="screens-label">SCREENS</span>
    </div>

    <p class="offer-list">
      Prize Giveaways / Breakfast Burger and<br>
      Beer Breakfast Pre Game / Wings,<br>
      Pizzas, Beer Towers, Buckets,<br>
      KTO940 Radio Live Crossover Onsite
    </p>

    <div class="reserve-button">Reserve your table now</div>

    <p class="phone-line">1 3000 FEAST</p>
  </main>
</body>
</html>
```